Evening at the Lanternhouse

I need a jpeg of a poster advertising a church party
It has a jazzy, fun theme. Details

A Evening at The Lanternhouse
Friday, June 14th from 8-11 PM
Party for all Elm Parish adults at the Stake Centre
Fun, food, friends,live music, a chance to mingle and relax!
A great chance to bring your friends for a fun evening!

Id like some sort of jazz picture or shadowy picture....not really sure but I need it super fast so that I can have it printed Saturday...can anyone help me? I want it to be fun and snappy looking without being racy...no naked women :)

• naked or half dressed women, cigarettes, alcohol

```html
<!DOCTYPE html>
<html lang="en">
<head>
<meta charset="utf-8">
<title>Evening at The Lanternhouse</title>
<link href="https://fonts.googleapis.com/css2?family=Lobster&family=Fredoka:wght@500;600;700&family=Kalam:wght@400;700&family=Poiret+One&display=swap" rel="stylesheet">
<style>
  :root {
    --red: #d41f1f;
    --red-deep: #b81414;
    --red-band: #c81a1e;
    --pink: #e8566a;
    --pink-soft: #f08a8a;
    --white: #ffffff;
    --yellow: #f2d21c;
    --olive: #d2b33a;
    --maroon: #5a0d0d;
    --orange: #f08a1e;
    --shadow: #1a0505;
  }
  html, body { margin: 0; padding: 0; overflow: hidden; }
  body { width: 848px; height: 1200px; background: var(--red); }
  .poster {
    position: relative; width: 848px; height: 1200px; overflow: hidden;
    background: linear-gradient(90deg, var(--red) 0 760px, var(--red-band) 760px);
  }
  .poster > * { position: absolute; margin: 0; line-height: 1; white-space: nowrap; }
  .deco { left: 0; top: 0; }
  .title-lead { left: 392px; top: 80px; font: 700 42px "Fredoka", sans-serif; color: var(--white); letter-spacing: 1px; }
  .title-main { left: 175px; top: 100px; font: 108px "Lobster", cursive; color: var(--pink); text-shadow: 2px 3px 0 var(--red-deep); }
  .party { left: 46px; top: 240px; font: 700 84px "Fredoka", sans-serif; color: var(--yellow); }
  .audience { left: 290px; top: 262px; font: 400 38px "Kalam", cursive; color: var(--white); }
  .audience .parish { color: var(--maroon); font-weight: 700; }
  .venue-lead { left: 180px; top: 324px; font: 400 38px "Kalam", cursive; color: var(--white); }
  .venue { left: 326px; top: 312px; font: 700 58px "Fredoka", sans-serif; color: var(--white); }
  .tagline { left: 108px; top: 396px; font: 700 76px "Fredoka", sans-serif; letter-spacing: 6px; color: transparent; -webkit-text-stroke: 3px var(--white); }
  .dancers { left: 0; top: 470px; width: 848px; height: 370px;
    background:
      radial-gradient(ellipse 60% 30% at 50% 92%, rgba(240,138,30,.95), rgba(240,138,30,0) 100%),
      linear-gradient(180deg, rgba(26,5,5,0) 0%, rgba(26,5,5,.75) 18%, rgba(26,5,5,.85) 60%, rgba(26,5,5,.2) 88%, rgba(26,5,5,0) 100%); }
  .month { left: 20px; top: 856px; font: 700 96px "Fredoka", sans-serif; color: var(--white); transform: skewX(-6deg); }
  .day-num { left: 378px; top: 858px; font: 400 56px "Kalam", cursive; color: var(--white); }
  .weekday { right: 14px; top: 858px; font: 700 84px "Fredoka", sans-serif; color: var(--white); transform: skewX(-8deg); }
  .with { left: 104px; top: 952px; font: 700 26px "Fredoka", sans-serif; color: var(--olive); }
  .time-start { left: 330px; top: 950px; font: 700 44px "Fredoka", sans-serif; color: var(--white); letter-spacing: 2px; }
  .time-end { left: 293px; top: 1006px; font: 700 44px "Fredoka", sans-serif; color: var(--white); letter-spacing: 2px; }
  .closing { left: 228px; top: 1064px; font: 400 44px "Kalam", cursive; color: var(--white); transform: rotate(-3deg); }
  .offer { left: 16px; top: 998px; font: 700 44px "Poiret One", sans-serif; color: var(--maroon); }
  .offer span { display: block; }
  .offer .family { font-size: 62px; }
  .offer .food { font-size: 66px; }
  .music { right: 8px; top: 1086px; font: 600 36px "Fredoka", sans-serif; color: var(--maroon); text-align: right; }
  .music span { display: block; }
  .music .big { font-size: 60px; letter-spacing: 3px; margin-top: 4px; }
</style>
</head>
<body>
<main class="poster">
  <svg class="deco" width="848" height="1200" aria-hidden="true">
    <g fill="var(--pink-soft)" opacity="0.55">
      <circle cx="170" cy="310" r="44"/>
      <circle cx="225" cy="285" r="40"/>
      <circle cx="215" cy="350" r="46"/>
      <circle cx="155" cy="365" r="36"/>
      <circle cx="265" cy="335" r="34"/>
    </g>
  </svg>

  <p class="title-lead">Evening at The</p>
  <h1 class="title-main">Lanternhouse</h1>

  <p class="party">Party</p>
  <p class="audience">for all <span class="parish">Elm Parish</span> adults</p>
  <p class="venue-lead">at the</p>
  <p class="venue">Stake Centre</p>
  <p class="tagline">LIVE AND LOUD</p>

  <div class="dancers" role="img" aria-label="Black silhouettes of a group of people dancing over an orange halftone glow"></div>

  <p class="month">JUNE</p>
  <p class="day-num">14th</p>
  <p class="weekday">FRIDAY</p>

  <p class="with">WITH</p>
  <p class="time-start">8:00 TO</p>
  <p class="time-end">11:00 PM</p>
  <p class="closing">for a fun evening!</p>

  <p class="offer"><span>FRIENDS</span><span class="family">FAMILY</span><span class="food">FOOD</span></p>
  <p class="music"><span>'N' LIVE</span><span class="big">MUSIC</span></p>
</main>
</body>
</html>
```